Increased budget: GUI redesign: 10 year old user interface needs modern look-and-feel

UPDATE: Please DO look at more than only th eone image I attached! Almost all designs are simply reworks of that one picture. That is not what we are looking for. Check out the video to understand what the product does, and try to make something better.
We have an existing app (see https://www.vextorane.com/downloadBrivoPanel.php?vers=3_9_1_140964&dir=Vextorane_OEM/3_9_1_140964&name=DSP_Control_Software) which needs refreshing. See also a video here: https://vextorane-oem.com/software/ and the user manual attached here. The GUI is now 800x400 pixels, which is too small; and not scalable, which will be fixed in the future. We need a new, modern look-and-feel, and images that can be exported from the design in various sizes. The current design is attached as well as a collection of PNG files. The overall layout can stay similar, although we are open to good ideas for improvements. The design should be targeted at professional users, not end users; the product is used by audio professionals (e.g. sound engineers, loudspeaker designers). Also see our web version: https://www.vextorane.com/brivopanel/skins/1_1_2/container.html?MAC=Demo%201x2
The winner will also be asked to do a full design of the application GUI (based on the design done here), with several more windows etc, and additional payment depending on the work to be done.

Target Market(s)

Professional audio

Industry/Entity Type

Audio / Industrial

Font styles to use
Other font styles liked:
• Futura (not mandatory)

Colors

Designer to choose colors to be used in the design.

Requirements
Must have
• Modern, timeless design, not too bling bling
Nice to have
• Flat design
Should not have
• 3D, bling bling, many colours, etc

```html
<!DOCTYPE html>
<html lang="en">
<head>
<meta charset="utf-8">
<title>Vextorane DSP Command Centre</title>
<link rel="stylesheet" href="https://fonts.googleapis.com/css2?family=Roboto:wght@400;500;700&display=swap">
<style>
  :root {
    --page-bg: #b5b5b5;
    --panel-bg: #ffffff;
    --sidebar-bg: #eeeeee;
    --band-bg: #e4e4e4;
    --footer-bg: #55565a;
    --ink: #555559;
    --ink-dark: #2a2a2a;
    --btn-dark: #55565a;
    --btn-light: #b9b9bb;
    --field-grey: #d6d6d8;
    --channel-btn: #7a7a7e;
    --main-gold: #deb052;
    --xover-dark: #222220;
    --ok-green: #3de83a;
    --alert-red: #ff1a1a;
    --divider: #d9d9d9;
  }
  * { box-sizing: border-box; margin: 0; padding: 0; }
  html, body { width: 1200px; height: 940px; overflow: hidden; }
  body { background: var(--page-bg); font-family: "Roboto", Arial, sans-serif; color: var(--ink); position: relative; }

  .app-window { position: absolute; left: 45px; top: 51px; width: 1117px; height: 847px; background: var(--panel-bg); }
  .sidebar { position: absolute; left: 0; top: 0; width: 208px; height: 743px; background: var(--sidebar-bg); }
  .sidebar-label { position: absolute; left: 24px; font-size: 13.5px; font-weight: 700; color: var(--ink); letter-spacing: .2px; }
  .divider { position: absolute; left: 0; width: 208px; height: 1px; background: var(--divider); }
  .pill { position: absolute; width: 83px; height: 28px; border-radius: 14px; color: #fff; font-size: 10.5px; font-weight: 500; display: flex; align-items: center; justify-content: center; }
  .pill--dark { background: var(--btn-dark); }
  .pill--light { background: var(--btn-light); }
  .field { position: absolute; width: 167px; height: 29px; font-size: 8.5px; font-weight: 500; color: #333; display: flex; align-items: center; padding-left: 12px; }
  .field--input { background: #fff; border: 1px solid #9a9a9a; }
  .field--grey { background: var(--field-grey); }
  .dot { position: absolute; border-radius: 50%; }

  .title { position: absolute; left: 0; width: 1276px; top: 30px; text-align: center; font-size: 25px; font-weight: 500; color: var(--ink); letter-spacing: .3px; }

  .footer { position: absolute; left: 0; top: 743px; width: 1117px; height: 104px; background: var(--footer-bg); }
  .round-btn { position: absolute; width: 60px; height: 60px; border-radius: 50%; color: #fff; font-size: 11.5px; font-weight: 500; display: flex; align-items: center; justify-content: center; transform: translate(-50%, -50%); }
  .round-btn--channel { background: var(--channel-btn); }
  .round-btn--main { background: var(--main-gold); }
  .round-btn--xover { background: var(--xover-dark); }

  .mixer { position: absolute; left: 0; top: 0; }
</style>
</head>
<body>
<div class="app-window">
  <aside class="sidebar">
    <div class="sidebar-label" style="top:37px">LOCAL PRESETS</div>
    <div class="pill pill--dark" style="left:26px;top:65px">STORE</div>
    <div class="pill pill--light" style="left:116px;top:65px">LOAD</div>
    <div class="divider" style="top:110px"></div>

    <div class="sidebar-label" style="top:130px">UNIT PRESETS</div>
    <div class="field field--input" style="left:27px;top:160px">NO NAME</div>
    <div class="field field--grey" style="left:27px;top:195px">1: EMPTY PRESET</div>
    <div class="pill pill--dark" style="left:23px;top:238px">STORE</div>
    <div class="pill pill--light" style="left:113px;top:238px">LOAD</div>
    <div class="divider" style="top:285px"></div>

    <div class="sidebar-label" style="top:295px">LINK</div>
    <div class="dot" style="left:163px;top:291px;width:23px;height:23px;background:var(--ok-green)"></div>
    <div class="field field--grey" style="left:24px;top:322px">KTR316</div>
    <div class="divider" style="top:371px"></div>

    <div class="sidebar-label" style="top:387px">UNIT NAME</div>
    <div class="field field--input" style="left:26px;top:410px">KTR312</div>
    <div class="divider" style="top:452px"></div>

    <div class="sidebar-label" style="top:462px">STATUS</div>
    <div class="dot" style="left:162px;top:459px;width:23px;height:23px;background:var(--alert-red)"></div>
    <div class="pill pill--light" style="left:111px;top:490px">DETAILS</div>
  </aside>

  <h1 class="title">VEXTORANE DSP COMMAND CENTRE</h1>

  <footer class="footer">
    <div class="round-btn round-btn--main" style="left:53px;top:50px">MAIN</div>
    <div class="round-btn round-btn--xover" style="left:119px;top:50px">X-OVER</div>
    <div class="round-btn round-btn--channel" style="left:270px;top:51px">IN 1</div>
    <div class="round-btn round-btn--channel" style="left:336px;top:52px">IN 2</div>
    <div class="round-btn round-btn--channel" style="left:401px;top:53px">IN 3</div>
    <div class="round-btn round-btn--channel" style="left:467px;top:54px">IN 4</div>
    <div class="round-btn round-btn--channel" style="left:561px;top:53px">OUT 1</div>
    <div class="round-btn round-btn--channel" style="left:627px;top:54px">OUT 2</div>
    <div class="round-btn round-btn--channel" style="left:697px;top:53px">OUT 3</div>
    <div class="round-btn round-btn--channel" style="left:764px;top:54px">OUT 4</div>
    <div class="round-btn round-btn--channel" style="left:831px;top:55px">OUT 5</div>
    <div class="round-btn round-btn--channel" style="left:897px;top:56px">OUT 6</div>
    <div class="round-btn round-btn--channel" style="left:963px;top:55px">OUT 7</div>
    <div class="round-btn round-btn--channel" style="left:1029px;top:56px">OUT 8</div>
  </footer>
</div>

<svg class="mixer" width="1200" height="940" viewBox="0 0 1200 940" font-family="Roboto, Arial, sans-serif">
  <defs>
    <pattern id="tick-fine" patternUnits="userSpaceOnUse" width="18" height="4.4">
      <rect x="3" y="0" width="12" height="1.1" fill="#a3a3a3"/>
    </pattern>
    <pattern id="tick-major" patternUnits="userSpaceOnUse" width="18" height="22">
      <rect x="0" y="0" width="18" height="1.2" fill="#8e8e8e"/>
    </pattern>
    <g id="fader-channel">
      <rect x="-9" y="160" width="18" height="477" fill="url(#tick-fine)"/>
      <rect x="-9" y="160" width="18" height="477" fill="url(#tick-major)"/>
      <rect x="14.5" y="159" width="6" height="488" rx="3" fill="#dedede"/>
      <rect x="29.5" y="159" width="6" height="488" rx="3" fill="#68686c"/>
      <rect x="11.5" y="202" width="12" height="62" rx="6" fill="#56565a"/>
    </g>
  </defs>

  <!-- control buttons -->
  <circle cx="1070" cy="87" r="17" fill="#8a8a8e"/>
  <g fill="#fff" transform="translate(1070 87)">
    <circle r="6.5"/>
    <g>
      <rect x="-1.8" y="-9" width="3.6" height="18" rx="1"/>
      <rect x="-1.8" y="-9" width="3.6" height="18" rx="1" transform="rotate(45)"/>
      <rect x="-1.8" y="-9" width="3.6" height="18" rx="1" transform="rotate(90)"/>
      <rect x="-1.8" y="-9" width="3.6" height="18" rx="1" transform="rotate(135)"/>
    </g>
    <circle r="2.6" fill="#8a8a8e"/>
  </g>
  <circle cx="1109" cy="87" r="17" fill="#2a2a2a"/>
  <circle cx="1109" cy="87" r="10" fill="none" stroke="#fff" stroke-width="2"/>
  <path d="M1104.5 82.5 L1113.5 91.5 M1113.5 82.5 L1104.5 91.5" stroke="#fff" stroke-width="2.2" stroke-linecap="round"/>

  <!-- level scale -->
  <g font-size="13" font-weight="500" fill="#555559" text-anchor="end">
    <text x="310" y="169">+12</text><text x="310" y="216">+6</text><text x="310" y="263">0</text>
    <text x="310" y="310">-6</text><text x="310" y="357">-12</text><text x="310" y="404">-18</text>
    <text x="310" y="451">-24</text><text x="310" y="498">-30</text><text x="310" y="545">-36</text>
    <text x="310" y="592">-42</text><text x="310" y="639">-48</text>
  </g>
  <g font-size="13" font-weight="500" fill="#555559" text-anchor="end">
    <text x="1118" y="165">+12</text><text x="1118" y="212">+6</text><text x="1118" y="259">0</text>
    <text x="1118" y="306">-6</text><text x="1118" y="353">-12</text><text x="1118" y="400">-18</text>
    <text x="1118" y="447">-24</text><text x="1118" y="494">-30</text><text x="1118" y="541">-36</text>
    <text x="1118" y="588">-42</text><text x="1118" y="635">-48</text>
  </g>

  <!-- input faders -->
  <use href="#fader-channel" x="331"/>
  <use href="#fader-channel" x="388"/>
  <use href="#fader-channel" x="443"/>
  <use href="#fader-channel" x="499"/>
  <!-- output faders -->
  <use href="#fader-channel" x="631"/>
  <use href="#fader-channel" x="688"/>
  <use href="#fader-channel" x="743"/>
  <use href="#fader-channel" x="799"/>
  <use href="#fader-channel" x="859" y="1"/>
  <use href="#fader-channel" x="915" y="1"/>
  <use href="#fader-channel" x="970" y="1"/>
  <use href="#fader-channel" x="1027" y="1"/>

  <!-- link / mute band -->
  <rect x="254" y="666" width="910" height="128" fill="#e4e4e4"/>
  <text x="270" y="701" font-size="11" font-weight="500" fill="#333">LINK</text>
  <line x1="313" y1="697" x2="1116" y2="697" stroke="#777" stroke-width="1"/>
  <g fill="#b4b4b6">
    <circle cx="358" cy="697" r="10.5"/><circle cx="446" cy="697" r="10.5"/>
    <circle cx="608" cy="697" r="10.5"/><circle cx="702" cy="697" r="10.5"/>
    <circle cx="864" cy="697" r="10.5"/><circle cx="1014" cy="697" r="10.5"/>
  </g>
  <circle cx="652" cy="697" r="10.5" fill="#737376"/>

  <text x="270" y="762" font-size="11" font-weight="500" fill="#333">MUTE</text>
  <line x1="313" y1="758" x2="1116" y2="758" stroke="#777" stroke-width="1"/>
  <g fill="#77777a">
    <circle cx="357" cy="758" r="10.5"/><circle cx="406" cy="758" r="10.5"/>
    <circle cx="456" cy="758" r="10.5"/><circle cx="506" cy="758" r="10.5"/>
    <circle cx="596" cy="758" r="10.5"/><circle cx="660" cy="758" r="10.5"/>
    <circle cx="724" cy="758" r="10.5"/><circle cx="788" cy="758" r="10.5"/>
    <circle cx="864" cy="758" r="10.5"/><circle cx="928" cy="758" r="10.5"/>
    <circle cx="992" cy="758" r="10.5"/><circle cx="1056" cy="758" r="10.5"/>
  </g>

  <!-- status indicator -->
  <rect x="208" y="579" width="12" height="30" rx="6" fill="#111"/>
  <circle cx="214" cy="606" r="15" fill="#111"/>
  <circle cx="214" cy="608" r="10" fill="#0a8a12"/>
</svg>
</body>
</html>
```